Bramblewick Acres Organic Hemp Company needs an OLD WORLD Label for CBD Bottle!

*UPDATE* Increased the budget! Please keep in mind, we are also open to "modern vintage", "hipster vintage" and other forms of retro emulation. Whatever the case, we are looking for a small work of art, like an indie Gin bottle- not the clinical drab that every other CBD bottle has. Also, don't be afraid to incorporate color, or alter the logo (color wise), we want something breathtaking in a small package. Show us what that looks like to you!

*UPDATE* Please take a moment to visit this link to see the types of branding we are interested in: https://www.pinboardly.example/tobiasquentinharlow/neat-branding/

We are an Organic Hemp company about to launch it's first line of products. This design is for our CBD Bottle. We have a pre-existing logo that we need developed and expanded into a label. Our theme is Old World, Victorian, Vintage, Turn of the Century (there are too many names for this genre, you get it...) We want our brand to convey a sense of intrigue, artisan quality and a bit of mystery. Very different from the clinical look of most CBD tinctures. We are HUGE fans of the design house "Copper and Copper" and would LOVE something that conjures that feel.

The first attachment will be our current logo, and I will be adding "inspiration" as I can.

The second attachment will be a rendition of our raw logo with regulatory information. This is what we need this spiced up! You DO NOT have to follow this design, but the same information needs to be on there. It's very likely that the line work will be in "gold foil".

Any additional attachments are for "inspiration", what we're looking for.

Feel free to explore with it, we are looking for something breathtaking!

Thanks!

Tobias
Bramblewick Acres
Verdant Curios

Target Market(s)

Younger, Hipster Demographic and all who are interested in Organic Products!

Colors

Designer to choose colors to be used in the design.

Requirements
Must have
• Full Spectrum Hemp Extract CDB Oil 1000mg Natural Flavor 1.02 FL OZ (30 ML)
Should not have
• Cannabis, Cannabis leaves, Marijuana etc...

```html
<!DOCTYPE html>
<html lang="en">
<head>
<meta charset="utf-8">
<title>Bramblewick Acres CBD Oil Label</title>
<link href="https://fonts.googleapis.com/css2?family=Oswald:wght@500;600;700&family=Rye&display=swap" rel="stylesheet">
<style>
  :root {
    --backdrop: #d6d6d6;
    --label-black: #07080a;
    --gold: #c9a93c;
    --gold-light: #e6cf74;
    --gold-deep: #8d7224;
    --ivory: #f1efe8;
  }
  html, body {
    margin: 0;
    width: 1176px;
    height: 1200px;
    overflow: hidden;
    background: var(--backdrop);
  }
  .label {
    position: absolute;
    left: 308px;
    top: 175px;
    width: 560px;
    height: 850px;
    background: var(--label-black);
    box-shadow: 0 18px 40px rgba(0,0,0,0.25);
    font-family: "Oswald", sans-serif;
    color: var(--gold);
  }
  .frame {
    position: absolute;
    left: 26px; right: 26px; top: 140px; bottom: 14px;
    border: 2px solid var(--gold);
    outline: 1px solid var(--gold-deep);
    outline-offset: 5px;
  }
  .flourish {
    position: absolute;
    background: linear-gradient(90deg, rgba(201,169,60,0.15), rgba(201,169,60,0.55), rgba(201,169,60,0.15));
    border-radius: 40px;
  }
  .flourish-crown { left: 150px; width: 260px; top: 10px; height: 40px; }
  .flourish-mid { left: 70px; width: 420px; top: 586px; height: 40px; }
  .flourish-left { left: 40px; width: 64px; top: 684px; height: 64px; }
  .flourish-right { right: 40px; width: 64px; top: 684px; height: 64px; }
  .flourish-base { left: 120px; width: 320px; top: 756px; height: 34px; }
  .arc-title {
    position: absolute;
    left: 0; top: 40px;
    width: 560px; height: 90px;
  }
  .arc-title text {
    font-family: "Oswald", sans-serif;
    font-weight: 600;
    font-size: 25px;
    letter-spacing: 3px;
    fill: var(--gold);
  }
  .brand {
    position: absolute;
    left: 50px; right: 50px; top: 170px; height: 260px;
    display: flex;
    flex-direction: column;
    align-items: center;
    justify-content: center;
    gap: 18px;
  }
  .brand-row {
    display: flex;
    align-items: center;
    gap: 20px;
  }
  .brand-mark {
    width: 60px; height: 60px;
    border-radius: 50%;
    background: var(--gold);
    flex: none;
  }
  .brand-name {
    font-family: "Rye", serif;
    font-size: 44px;
    line-height: 1.1;
    color: var(--ivory);
    text-align: left;
  }
  .tagline {
    font-family: "Oswald", sans-serif;
    font-weight: 600;
    font-size: 20px;
    letter-spacing: 5px;
    color: var(--ivory);
  }
  .product {
    position: absolute;
    left: 40px; right: 40px; top: 460px; height: 110px;
    display: flex;
    align-items: center;
    gap: 18px;
  }
  .rules {
    flex: 1;
    height: 44px;
    background: repeating-linear-gradient(180deg, var(--gold) 0 2px, transparent 2px 9px);
  }
  .product-name {
    margin: 0;
    font-family: "Oswald", sans-serif;
    font-weight: 700;
    font-size: 92px;
    letter-spacing: 6px;
    line-height: 1;
    color: var(--gold-light);
  }
  .plaque {
    position: absolute;
    left: 50%;
    transform: translateX(-50%);
    border-top: 2px solid var(--gold);
    border-bottom: 2px solid var(--gold);
    text-align: center;
    font-weight: 600;
    white-space: nowrap;
  }
  .flavor { top: 636px; width: 380px; font-size: 28px; letter-spacing: 4px; padding: 2px 0; }
  .strength { top: 692px; width: 250px; font-size: 40px; letter-spacing: 4px; line-height: 1.3; }
  .volume {
    position: absolute;
    left: 60px; right: 60px; top: 796px;
    display: flex;
    align-items: center;
    gap: 16px;
    font-weight: 500;
    font-size: 22px;
    letter-spacing: 3px;
  }
  .volume .line { flex: 1; height: 2px; background: var(--gold); }
  .volume span + span { margin-left: 22px; }
</style>
</head>
<body>
  <main class="label">
    <div class="flourish flourish-crown" role="img" aria-label="Gold scrollwork crest"></div>
    <div class="frame"></div>

    <svg class="arc-title" viewBox="0 0 560 90">
      <path id="title-arc" d="M70 78 Q280 22 490 78" fill="none"/>
      <text text-anchor="middle"><textPath href="#title-arc" startOffset="50%">FULL SPECTRUM HEMP EXTRACT</textPath></text>
    </svg>

    <section class="brand">
      <div class="brand-row">
        <div class="brand-mark"></div>
        <div class="brand-name">Bramblewick<br>Acres</div>
      </div>
      <div class="tagline">VERDANT CURIOS</div>
    </section>

    <section class="product">
      <div class="rules"></div>
      <h1 class="product-name">CBD OIL</h1>
      <div class="rules"></div>
    </section>

    <div class="flourish flourish-mid" role="img" aria-label="Gold ornamental scroll divider"></div>
    <div class="plaque flavor">NATURAL FLAVOR</div>
    <div class="flourish flourish-left" role="img" aria-label="Gold corner scroll"></div>
    <div class="plaque strength">1000 MG</div>
    <div class="flourish flourish-right" role="img" aria-label="Gold corner scroll"></div>
    <div class="flourish flourish-base" role="img" aria-label="Gold ornamental scroll base"></div>

    <footer class="volume">
      <div class="line"></div>
      <div><span>1 FL OZ</span><span>30 ML</span></div>
      <div class="line"></div>
    </footer>
  </main>
</body>
</html>
```